A small boutique Accounting and Mortgage Broking firm needs a business card design

Quorvel is a Brisbane based boutique accounting and mortgage broking firm. We offer a range of extensive financial services like accounting, tax consulting, book-keeping and mortgage broking.
We need a business card that stands out. The content can stay as it is on the existing card unless you recommend us to change anything on it for a better design.
Please remove the mobile number and give us a suitable format to change the details like email address and name.
Industry/Entity Type
Business
Contact Information for Business Card
Dalian Okoruwe
Quorvel Group Pty Ltd
3/412 Brackwin Rd Salisbury QLD 4107
PO Box 829 Salisbury QLD 4107
T 07 3184 5526
F 07 3952 1087
E dokoruwe@quorvel.net.au
Accountants Tax Agents, Mortgage Brokers
www.quorvel.net.au
Look and feel
Each slider illustrates characteristics of the customer's brand and the style your logo design should communicate.

```html
<!DOCTYPE html>
<html lang="en">
<head>
<meta charset="utf-8">
<title>Quorvel Business Card</title>
<link rel="stylesheet" href="https://fonts.googleapis.com/css2?family=Open+Sans:wght@400;600;700;800&family=Libre+Baskerville:ital,wght@0,700;1,700&display=swap">
<style>
  :root {
    --stage: #e9e7e2;
    --card-white: #ffffff;
    --card-shade: #f1f1f1;
    --green: #7ac143;
    --green-dark: #5ea12c;
    --charcoal: #3a3a3a;
    --grey: #5b5b5b;
    --text-dark: #2f2f2f;
  }
  * { margin: 0; padding: 0; box-sizing: border-box; }
  html, body {
    width: 1200px; height: 1023px; overflow: hidden;
    background: var(--stage);
    font-family: "Open Sans", Arial, sans-serif;
    color: var(--charcoal);
  }
  .stage {
    width: 1200px; height: 1023px;
    display: flex; flex-direction: column; align-items: center; justify-content: center;
    gap: 50px;
  }
  .card {
    position: relative;
    width: 780px; height: 446px;
    border-radius: 6px;
    overflow: hidden;
    box-shadow: 0 10px 28px rgba(0,0,0,0.18);
  }

  /* Front card */
  .card-front {
    background: linear-gradient(115deg, var(--green-dark) 0%, var(--green) 38%, #c9e6ae 52%, var(--card-white) 62%, var(--card-white) 100%);
  }
  .front-details { position: absolute; left: 48px; top: 44px; }
  .brand { display: flex; align-items: center; gap: 12px; }
  .brand-dot {
    width: 38px; height: 38px; border-radius: 50%;
    background: var(--charcoal);
  }
  .brand-name {
    font-weight: 800; font-size: 40px; letter-spacing: -0.5px;
    color: var(--charcoal); line-height: 1;
  }
  .tagline {
    margin-top: 8px;
    font-size: 17px; letter-spacing: 1px; color: var(--grey);
  }
  .person-name {
    margin-top: 26px;
    font-family: "Libre Baskerville", Georgia, serif;
    font-weight: 700; font-size: 22px; letter-spacing: 1.5px;
    font-variant: small-caps; color: var(--grey);
  }
  .contact-list { list-style: none; margin-top: 14px; }
  .contact-list li {
    display: flex; align-items: center; gap: 12px;
    font-size: 17px; line-height: 30px; color: var(--text-dark);
  }
  .contact-icon { width: 16px; height: 16px; flex: none; }
  .address { margin-top: 18px; font-size: 17px; line-height: 27px; color: var(--text-dark); }

  /* Back card */
  .card-back {
    background: radial-gradient(circle at 45% 40%, var(--card-white) 0%, var(--card-shade) 100%);
    display: flex; flex-direction: column; align-items: center; justify-content: center;
  }
  .back-brand { display: flex; align-items: center; gap: 22px; }
  .back-brand .brand-dot { width: 90px; height: 90px; }
  .back-brand .brand-name { font-size: 104px; letter-spacing: -2px; }
  .back-tagline {
    margin-top: 14px;
    font-size: 44px; letter-spacing: 1px; color: var(--charcoal);
  }
  .services {
    position: absolute; bottom: 30px; left: 0; right: 0; text-align: center;
    font-family: "Libre Baskerville", Georgia, serif;
    font-style: italic; font-weight: 700; font-size: 17px;
    letter-spacing: 1px; color: #222;
  }
</style>
</head>
<body>
<main class="stage">
  <section class="card card-front" aria-label="Business card front">
    <div class="front-details">
      <div class="brand">
        <span class="brand-dot"></span>
        <span class="brand-name">quorvel</span>
      </div>
      <p class="tagline">CLARITY. CARE. PROGRESS.</p>
      <p class="person-name">Dalian Okoruwe</p>
      <ul class="contact-list">
        <li>
          <svg class="contact-icon" viewBox="0 0 16 16"><path d="M4 1h3l1 4-2 1.5a9 9 0 0 0 3.5 3.5L11 8l4 1v3a2 2 0 0 1-2 2A12 12 0 0 1 2 3a2 2 0 0 1 2-2z" fill="#666"/></svg>
          07 3184 5526
        </li>
        <li>
          <svg class="contact-icon" viewBox="0 0 16 16"><rect x="4" y="1" width="8" height="5" fill="#666"/><rect x="1" y="6" width="14" height="7" rx="1" fill="#666"/><rect x="4" y="10" width="8" height="5" fill="#fff" stroke="#666"/></svg>
          07 3952 1087
        </li>
        <li>
          <svg class="contact-icon" viewBox="0 0 16 16"><rect x="1" y="3" width="14" height="10" fill="#666"/><path d="M1 3l7 6 7-6" fill="none" stroke="#fff" stroke-width="1.4"/></svg>
          dokoruwe@quorvel.net.au
        </li>
        <li>
          <svg class="contact-icon" viewBox="0 0 16 16"><circle cx="8" cy="8" r="7" fill="#666"/><path d="M1 8h14M8 1c3 3 3 11 0 14M8 1c-3 3-3 11 0 14" fill="none" stroke="#fff" stroke-width="1"/></svg>
          www.quorvel.net.au
        </li>
      </ul>
      <p class="address">3/412 Brackwin Rd<br>Keswyn QLD 4119<br>PO Box 829 Keswyn QLD 4119</p>
    </div>
  </section>

  <section class="card card-back" aria-label="Business card back">
    <div class="back-brand">
      <span class="brand-dot"></span>
      <span class="brand-name">quorvel</span>
    </div>
    <p class="back-tagline">CLARITY. CARE. PROGRESS.</p>
    <p class="services">ACCOUNTANTS - TAX AGENTS - MORTGAGE BROKERS</p>
  </section>
</main>
</body>
</html>
```